Brochure design

We need a 4 page A4 brochure for our engieering companyA draft version of the text can be found in the attachments, along with the logo.The text pdf shows the general style and layout of hte text, but am very open to artistic advice.Three image placeholders should be added on pages indicated - these are not yet availableThe logo gives a good idea of the colour scheme required.For background graphics, the use of swirl patterns is desirable.Look and feel should be clean and professional, not too cluttered.Final desing shoul dbe avialable in RGB psd format, with full layers so we can modify text and images easily.

```html
<!DOCTYPE html>
<html lang="en">
<head>
<meta charset="utf-8">
<title>Kinetic Thermal – Brochure</title>
<link rel="stylesheet" href="https://fonts.googleapis.com/css2?family=Oswald:wght@400;500&family=Roboto+Condensed:wght@400;700&family=Open+Sans:ital,wght@0,400;0,600;1,400&display=swap">
<style>
:root{
  --blue:#1a6cc0;
  --blue-deep:#0f55a6;
  --teal:#23b3a0;
  --purple:#4a3d8f;
  --ink:#2e2e2e;
  --grey:#5a5a5a;
  --ring:#d9dde2;
  --paper:#ffffff;
  --stage:#3a3a3a;
}
*{margin:0;padding:0;box-sizing:border-box}
html,body{width:1200px;height:1200px;overflow:hidden;background:var(--stage)}
.canvas{position:relative;width:1200px;height:1200px}
.page{position:absolute;width:365px;height:504px;background:var(--paper);overflow:hidden;font-family:"Open Sans",sans-serif;color:var(--ink);box-shadow:0 4px 14px rgba(0,0,0,.35)}
.p1{left:181px;top:74px}.p2{left:636px;top:74px}.p3{left:181px;top:646px}.p4{left:636px;top:646px}
.abs{position:absolute}
.bg{position:absolute;left:0;top:0;width:365px;height:504px}
.brand{position:absolute;display:flex;align-items:center;gap:5px;font-family:"Roboto Condensed",sans-serif;font-weight:700;color:var(--blue-deep);letter-spacing:.5px}
.brand .mark{width:9px;height:9px;background:var(--teal)}
.photo{position:absolute}
.small{font-size:6.4px;line-height:1.35}
.ticks{list-style:none}
.ticks li{position:relative;padding-left:14px;font-size:5px;font-style:italic;line-height:1.3;margin-bottom:4px}
.ticks li svg{position:absolute;left:0;top:0;width:8px;height:8px}
.white{color:#fff}
.center{text-align:center}
.oswald{font-family:"Oswald",sans-serif}
.cond{font-family:"Roboto Condensed",sans-serif}
.h-blue{color:var(--blue);font-size:7px;font-weight:600}
.icon-ring{position:absolute;border-radius:50%;background:#fff;border:4px solid var(--ring);display:flex;align-items:center;justify-content:center}
.icon-ring span{display:block;border-radius:50%;width:100%;height:100%}
.sec-title{font-family:"Roboto Condensed",sans-serif;color:var(--blue);font-size:10.5px;line-height:1.25}
.sec-item{font-size:5.3px;font-style:italic;line-height:1.3}
.round-icon{position:absolute;width:22px;height:22px;border-radius:50%;background:var(--ink)}
</style>
</head>
<body>
<div class="canvas">

  <!-- Page 1 -->
  <section class="page p1">
    <div class="photo" role="img" aria-label="Isometric illustration of a power plant with pylons and cooling towers" style="left:0;top:40px;width:205px;height:170px;background:linear-gradient(160deg,#e9eef2 0%,#c8d8cf 55%,#8fc4a0 100%)"></div>
    <svg class="bg" viewBox="0 0 365 504" aria-hidden="true">
      <path d="M0 190 C60 215 140 212 215 190 L215 203 C140 225 60 226 0 206Z" fill="var(--purple)"/>
      <path d="M0 200 C70 226 150 222 215 198 L215 210 C150 234 70 236 0 214Z" fill="var(--teal)"/>
      <path d="M205 170 A120 120 0 0 1 365 140 L365 504 L300 504 C280 470 250 420 205 300Z" fill="var(--teal)"/>
      <path d="M205 170 A120 120 0 0 1 365 140 L365 250 C320 300 240 310 205 285Z" fill="var(--blue)"/>
      <path d="M0 490 C120 478 250 462 365 440 L365 504 L0 504Z" fill="var(--blue)"/>
      <path d="M0 483 C120 471 250 455 365 432 L365 440 C250 462 120 478 0 490Z" fill="var(--teal)" opacity=".8"/>
    </svg>
    <div class="brand" style="left:205px;top:34px;font-size:15px"><span class="mark"></span>KINETIC THERMAL</div>

    <div class="abs white oswald center" style="left:225px;top:140px;width:130px;font-size:11.5px;line-height:1.6">WE ARE PLEASED<br>TO OFFER THE<br>FOLLOWING SERVICES :</div>
    <div class="abs white center" style="left:225px;top:200px;width:130px;font-size:6.2px;font-style:italic;line-height:1.3">
      <div style="width:10px;height:10px;margin:0 auto 3px;background:#fff;border-radius:2px"></div>Design and consultancy
      <div style="width:10px;height:10px;margin:6px auto 3px;background:#fff;border-radius:2px"></div>Development
      <div style="width:10px;height:10px;margin:6px auto 3px;background:#fff;border-radius:50%"></div>Implementation and support<br>of our custom thermal<br>simulation tools
    </div>
    <div class="abs white center" style="left:218px;top:330px;width:140px;font-size:7px;line-height:1.4">
      CONTACT US :<br>✉ dana.moreau@kt-thermal.co.uk<br><span style="display:block;margin-top:8px">VISIT US FOR<br>MORE INFORMATION</span><span style="display:block;margin-top:6px">● www.kt-thermal.co.uk</span>
    </div>

    <p class="abs small" style="left:20px;top:231px;width:178px">Kinetic Thermal Systems is a thermal engineering company specialising in the thermal management of electrical machines and electronic systems.</p>
    <div class="abs cond" style="left:0;top:278px;width:185px;height:18px;background:var(--teal);border-radius:0 9px 9px 0;color:var(--ink);font-size:10px;font-weight:700;padding:2px 0 0 21px">DESIGN AND CONSULTANCY</div>
    <p class="abs" style="left:21px;top:306px;width:180px;color:var(--blue);font-size:6.6px;line-height:1.3">We provide effective thermal design solutions for electrical machines and electronic systems</p>
    <ul class="abs ticks" style="left:21px;top:338px;width:180px">
      <li><svg viewBox="0 0 8 8"><circle cx="4" cy="4" r="3.5" fill="none" stroke="var(--teal)"/><path d="M2 4l1.5 1.5L6 2.7" fill="none" stroke="var(--teal)"/></svg>We cover every stage of a design for feasibility studies, from concept comparisons to design optimisation</li>
      <li><svg viewBox="0 0 8 8"><circle cx="4" cy="4" r="3.5" fill="none" stroke="var(--teal)"/><path d="M2 4l1.5 1.5L6 2.7" fill="none" stroke="var(--teal)"/></svg>We can review and improve cooling systems for existing designs</li>
      <li><svg viewBox="0 0 8 8"><circle cx="4" cy="4" r="3.5" fill="none" stroke="var(--teal)"/><path d="M2 4l1.5 1.5L6 2.7" fill="none" stroke="var(--teal)"/></svg>We work with our own specially developed toolset or with software of customers preference</li>
      <li><svg viewBox="0 0 8 8"><circle cx="4" cy="4" r="3.5" fill="none" stroke="var(--teal)"/><path d="M2 4l1.5 1.5L6 2.7" fill="none" stroke="var(--teal)"/></svg>We offer CFD, thermal network modelling, simple analytical analysis</li>
    </ul>
    <p class="abs small" style="left:21px;top:411px;width:212px">We are excellent collaborators and able to work closely with design teams from different technical disciplines to deliver solutions optimised towards product requirements and specifications</p>
  </section>

  <!-- Page 2 -->
  <section class="page p2">
    <div class="abs oswald center" style="left:0;top:22px;width:365px;font-size:14.5px;line-height:1.4">
      <div style="color:var(--blue)">WE HAVE A WIDE BREADTH OF EXPERIENCES.</div>
      <div style="color:var(--ink)">THE TABLES BELOW GIVES AN INDICATION</div>
    </div>
    <div class="brand" style="left:27px;top:85px;font-size:12px"><span class="mark"></span>KINETIC THERMAL</div>
    <svg class="bg" viewBox="0 0 365 504" aria-hidden="true">
      <path d="M78 205 V268 H108 L118 248 H176" fill="none" stroke="var(--blue)" stroke-width="4"/>
      <path d="M176 248 L186 228 H246 L258 220 H270" fill="none" stroke="var(--teal)" stroke-width="4"/>
      <line x1="176" y1="180" x2="176" y2="243" stroke="var(--grey)" stroke-width="2"/>
      <line x1="270" y1="160" x2="270" y2="218" stroke="var(--grey)" stroke-width="2"/>
      <circle cx="78" cy="268" r="6" fill="var(--blue)" stroke="var(--ring)" stroke-width="3"/>
      <circle cx="176" cy="243" r="6" fill="var(--teal)" stroke="var(--ring)" stroke-width="3"/>
      <circle cx="270" cy="222" r="6" fill="var(--grey)" stroke="var(--ring)" stroke-width="3"/>
    </svg>
    <div class="icon-ring" style="left:46px;top:146px;width:64px;height:64px"><span style="background:var(--blue)"></span></div>
    <div class="icon-ring" style="left:144px;top:118px;width:64px;height:64px"><span style="background:var(--teal)"></span></div>
    <div class="icon-ring" style="left:238px;top:98px;width:64px;height:64px"><span style="background:var(--ink)"></span></div>

    <div class="abs center" style="left:30px;top:284px;width:96px;font-size:5.4px;line-height:1.3">
      <div class="cond" style="color:var(--blue);font-size:8px;margin-bottom:3px">TECHNOLOGIES</div>
      Conventional Machines<br>Synchronous (PM, Field Wound, Reluctance)<br>Induction<br>Novel Machines Hybrid technology<br>Power Electronic Systems
    </div>
    <div class="abs center" style="left:132px;top:268px;width:90px;font-size:5.4px;line-height:1.3">
      <div class="cond" style="color:var(--blue);font-size:8px;margin-bottom:3px">APPLICATIONS</div>
      Power generation: Marine, stationary power plant, oil/gas offshore, hydro, wind<br>Industrial: pump drives, servo machines<br>Traction and Propulsion: EV, Marine
    </div>
    <div class="abs center" style="left:228px;top:238px;width:94px;font-size:5.4px;line-height:1.3">
      <div class="cond" style="color:var(--blue);font-size:8px;margin-bottom:3px">THERMAL<br>MANAGEMENT</div>
      Passive and active cooling Fan driven flow Water cooling Spray cooling Jet impingement<br>Advanced cooling measures
    </div>

    <div class="photo" role="img" aria-label="Photograph of an oil refinery lit at dusk beside water" style="left:0;top:372px;width:365px;height:132px;background:linear-gradient(180deg,#6d9fd8 0%,#3f6fa8 45%,#2b3e5a 75%,#1d5a8e 100%)"></div>
    <svg class="bg" viewBox="0 0 365 504" aria-hidden="true">
      <path d="M0 370 H365 V374 C250 396 120 398 0 384Z" fill="#fff"/>
    </svg>
    <div class="abs center" style="left:208px;top:344px;width:134px;color:var(--blue);font-size:5.6px;font-style:italic;line-height:1.3">Experience of working with and for companies and academic institutions across 8 countries</div>
  </section>

  <!-- Page 3 -->
  <section class="page p3">
    <svg class="bg" viewBox="0 0 365 504" aria-hidden="true">
      <defs><linearGradient id="p3sky" x1="0" y1="0" x2="1" y2="1"><stop offset="0" stop-color="#2a7fd0"/><stop offset="1" stop-color="#0f55a6"/></linearGradient></defs>
      <path d="M0 0 H365 V50 C300 60 250 80 200 108 C140 130 60 120 0 100Z" fill="url(#p3sky)"/>
      <path d="M0 100 C60 120 140 130 200 108 C250 80 300 60 365 50 V64 C300 74 250 96 200 122 C130 150 50 140 0 118Z" fill="var(--grey)"/>
      <path d="M0 118 C50 140 130 150 200 122 C250 96 300 74 365 64 V72 C300 84 250 106 200 130 C130 160 50 150 0 126Z" fill="#fff"/>
      <path d="M0 492 C100 500 240 494 365 482 V504 H0Z" fill="var(--blue)"/>
      <path d="M0 486 C100 494 240 488 365 476 V482 C240 494 100 500 0 492Z" fill="#cfe0f2"/>
    </svg>
    <div class="abs white" style="left:22px;top:26px;font-family:'Roboto Condensed',sans-serif;line-height:1.25">
      <div style="font-size:23px;font-weight:700;letter-spacing:.5px">CUTOM</div>
      <div style="font-size:21px">SIMULATION TOOLS</div>
    </div>
    <div class="brand" style="left:208px;top:117px;font-size:14px"><span class="mark"></span>KINETIC THERMAL</div>

    <p class="abs" style="left:22px;top:172px;width:322px;font-size:5.8px;line-height:1.32;text-align:justify">KTS have developed a simulation workflow which allows the accuracy of CFD to be exploited and integrated with thermal simulation tools. We therefore offer a more accurate analysis of machines without compromising on speed.<br>We are motivated to improve the speed and cost effectiveness of CFD modelling for electrical machine design. Our customised tools and workflow allow the accuracy of CFD to be exploited and integrated with quicker thermal modelling tools. This allows quick design exploration and optimisation whilst maintaining accuracy.</p>

    <div class="round-icon" style="left:24px;top:242px"></div>
    <div class="abs sec-title" style="left:57px;top:242px;width:260px">Customised OpenFlux CFD toolset, tailored for<br>electrical machines and electronics</div>
    <div class="abs sec-item" style="left:70px;top:274px;width:280px">Improved speed: minimised setup time<br><span style="display:block;margin-top:4px">Affordable: No expensive commercial licenses – costs don't scale up with computing power</span><span style="display:block;margin-top:4px">Greater automation: Customised workflow for electrical machines;<br>reduced user input; parameterised analysis</span></div>

    <div class="round-icon" style="left:24px;top:323px"></div>
    <div class="abs sec-title" style="left:57px;top:327px;width:280px">Thermal modelling using our in-house thermal network tool</div>
    <div class="abs sec-item" style="left:70px;top:354px;width:285px;line-height:2.6">High speed design exploration to expedite the route towards design optimisation<br>Flexible: able to simulation conventional and novel machines, as well as incorporate innovative<br>thermal management systems<br>In-built library of correlations for predicting flow and loss behaviour</div>

    <div class="round-icon" style="left:24px;top:414px"></div>
    <div class="abs sec-title" style="left:57px;top:418px">Coupling between tools</div>
    <div class="abs sec-item" style="left:70px;top:436px;width:288px;line-height:2.4">Feed reduced order flow models from CFD into thermal networks · Improved accuracy boundary<br>conditions versus packages that rely on broad empirical correlations · Ability to couple to wide<br>range of thermal modelling packages including commercial codes</div>
  </section>

  <!-- Page 4 -->
  <section class="page p4">
    <div class="photo" role="img" aria-label="Photograph of an industrial power station with tall chimneys under blue sky" style="left:0;top:0;width:365px;height:120px;background:linear-gradient(180deg,#5f95d0 0%,#9cc1e4 45%,#c9c9c2 75%,#8a8e90 100%)"></div>
    <svg class="bg" viewBox="0 0 365 504" aria-hidden="true">
      <path d="M0 80 C80 70 140 80 200 100 C260 120 320 110 365 95 V125 C300 140 240 135 180 120 C120 104 60 98 0 104Z" fill="var(--teal)"/>
      <path d="M0 92 C70 84 140 92 200 112 C260 132 320 122 365 108 V130 C300 146 240 142 180 128 C120 112 60 108 0 114Z" fill="var(--blue)"/>
      <path d="M0 112 C60 106 120 112 180 128 C240 144 300 148 365 130 V504 H0Z" fill="#fff"/>
      <path d="M0 432 C100 420 250 440 365 454 V504 H0Z" fill="var(--blue)"/>
      <path d="M0 426 C100 414 250 434 365 447 V454 C250 440 100 420 0 432Z" fill="var(--teal)"/>
    </svg>
    <p class="abs" style="left:23px;top:139px;width:230px;font-size:7.2px;line-height:1.3">We offer a range of services, and work with our customers to offer flexible and bespoke solutions in line with their needs</p>

    <div class="abs h-blue" style="left:23px;top:180px">Design services and support contracts</div>
    <ul class="abs ticks" style="left:30px;top:197px;width:310px">
      <li><svg viewBox="0 0 8 8"><circle cx="4" cy="4" r="3.5" fill="none" stroke="var(--teal)"/><path d="M2 4l1.5 1.5L6 2.7" fill="none" stroke="var(--teal)"/></svg>We work with you on your design project to enhance product performance using our experience, specialist toolsets and know-how</li>
      <li><svg viewBox="0 0 8 8"><circle cx="4" cy="4" r="3.5" fill="none" stroke="var(--teal)"/><path d="M2 4l1.5 1.5L6 2.7" fill="none" stroke="var(--teal)"/></svg>We can both develop new products and improve existing ranges</li>
      <li><svg viewBox="0 0 8 8"><circle cx="4" cy="4" r="3.5" fill="none" stroke="var(--teal)"/><path d="M2 4l1.5 1.5L6 2.7" fill="none" stroke="var(--teal)"/></svg>Able to use KTS toolset and workflow or follow company processes and design tools</li>
    </ul>

    <div class="abs h-blue" style="left:23px;top:253px">Use of KTS as 'simulation house'</div>
    <ul class="abs ticks" style="left:30px;top:268px;width:310px">
      <li><svg viewBox="0 0 8 8"><circle cx="4" cy="4" r="3.5" fill="none" stroke="var(--teal)"/><path d="M2 4l1.5 1.5L6 2.7" fill="none" stroke="var(--teal)"/></svg>Providing simulation analysis for your projects</li>
      <li><svg viewBox="0 0 8 8"><circle cx="4" cy="4" r="3.5" fill="none" stroke="var(--teal)"/><path d="M2 4l1.5 1.5L6 2.7" fill="none" stroke="var(--teal)"/></svg>KTS provide computing power: through our high-end cluster and access to wider range of clusters</li>
    </ul>

    <div class="abs h-blue" style="left:23px;top:303px">Integration of KTS toolsets</div>
    <ul class="abs ticks" style="left:30px;top:321px;width:310px">
      <li><svg viewBox="0 0 8 8"><circle cx="4" cy="4" r="3.5" fill="none" stroke="var(--teal)"/><path d="M2 4l1.5 1.5L6 2.7" fill="none" stroke="var(--teal)"/></svg>Adopting toolsets to your company, including training and ongoing support</li>
      <li><svg viewBox="0 0 8 8"><circle cx="4" cy="4" r="3.5" fill="none" stroke="var(--teal)"/><path d="M2 4l1.5 1.5L6 2.7" fill="none" stroke="var(--teal)"/></svg>Demos and evaluation periods available</li>
    </ul>

    <div class="abs h-blue" style="left:30px;top:361px">Collaboration on development</div>
    <ul class="abs ticks" style="left:30px;top:377px;width:310px">
      <li><svg viewBox="0 0 8 8"><circle cx="4" cy="4" r="3.5" fill="none" stroke="var(--teal)"/><path d="M2 4l1.5 1.5L6 2.7" fill="none" stroke="var(--teal)"/></svg>Advanced simulation of cooling methods, such as spray or evaporative cooling</li>
      <li><svg viewBox="0 0 8 8"><circle cx="4" cy="4" r="3.5" fill="none" stroke="var(--teal)"/><path d="M2 4l1.5 1.5L6 2.7" fill="none" stroke="var(--teal)"/></svg>Customisation of toolsets for special machine types or cooling arrangements</li>
    </ul>

    <div class="brand" style="left:222px;top:414px;font-size:13px"><span class="mark"></span>KINETIC THERMAL</div>
    <p class="abs white" style="left:20px;top:446px;width:180px;font-size:6.6px;font-style:italic;line-height:1.35">We welcome enquiries about our services, please contact us to learn more:</p>
    <div class="abs white" style="left:20px;top:472px;font-size:7px;display:flex;align-items:center;gap:6px"><span style="width:10px;height:10px;border-radius:50%;background:#fff"></span>dana.moreau@kt-thermal.co.uk</div>
    <div class="abs white" style="left:186px;top:472px;font-size:7px;display:flex;align-items:center;gap:6px"><span style="width:10px;height:10px;border-radius:50%;background:#fff"></span>www.kt-thermal.co.uk</div>
  </section>

</div>
</body>
</html>
```